Tandrel needs stationery design

We need desings for presentation cards and letter head for our company. It would be better that the letterhead uses our logo with white background and the presentation card the logo with the black background for the back of the card and the text (name, phone

Colors
0455a3
ec1f27
000000

Requirements
Must have
• Use company logo and colors

```html
<!DOCTYPE html>
<html lang="en">
<head>
<meta charset="utf-8">
<title>Tandrel business card</title>
<link href="https://fonts.googleapis.com/css2?family=Lato:wght@400;700&family=Oswald:wght@600&display=swap" rel="stylesheet">
<style>
  :root {
    --brand-blue: #0455a3;
    --brand-red: #ec1f27;
    --brand-black: #000000;
    --card-white: #ffffff;
    --ink-grey: #4a4a4a;
    --rule-grey: #b5b5b5;
    --logo-light: #e6e6e6;
    --page-bg: #d9d9d6;
  }
  * { box-sizing: border-box; margin: 0; padding: 0; }
  html, body { width: 1200px; height: 801px; overflow: hidden; }
  body {
    background: var(--page-bg);
    position: relative;
    font-family: "Lato", sans-serif;
  }
  .card {
    position: absolute;
    top: 257px;
    width: 500px;
    height: 286px;
    border-bottom: 4px solid var(--brand-red);
    box-shadow: 0 10px 24px rgba(0,0,0,0.18);
  }
  .card-front {
    left: 70px;
    background: var(--card-white);
    display: flex;
    align-items: center;
    padding-left: 62px;
  }
  .card-back {
    left: 630px;
    background: var(--brand-black);
    display: flex;
    align-items: center;
    justify-content: center;
  }
  .identity { text-align: right; }
  .person-name {
    font-family: "Oswald", sans-serif;
    font-weight: 600;
    font-size: 27px;
    letter-spacing: 0.5px;
    color: var(--brand-blue);
    line-height: 1.05;
    text-transform: uppercase;
  }
  .person-role {
    font-size: 15px;
    color: var(--ink-grey);
    letter-spacing: 0.5px;
  }
  .divider {
    width: 1px;
    height: 82px;
    background: var(--rule-grey);
    margin: 0 20px 0 22px;
  }
  .contact-list { list-style: none; }
  .contact-item {
    display: flex;
    align-items: center;
    font-size: 13px;
    color: var(--ink-grey);
    line-height: 20px;
    letter-spacing: 0.3px;
  }
  .contact-icon {
    width: 12px;
    height: 12px;
    margin-right: 8px;
    fill: var(--brand-red);
    flex: none;
  }
  .brand-name {
    font-family: "Lato", sans-serif;
    font-weight: 400;
    font-size: 56px;
    letter-spacing: 6px;
    color: var(--logo-light);
    text-transform: uppercase;
  }
</style>
</head>
<body>
  <section class="card card-front">
    <div class="identity">
      <p class="person-name">Marlow Quinn</p>
      <p class="person-role">President</p>
    </div>
    <div class="divider"></div>
    <ul class="contact-list">
      <li class="contact-item">
        <svg class="contact-icon" viewBox="0 0 12 12" aria-hidden="true"><path d="M2.5 1l2 2.4-1.1 1.3a7 7 0 0 0 3.9 3.9l1.3-1.1 2.4 2-1.3 1.5C5.4 10.9 1.1 6.6 1 2.3z"/></svg>
        555 210 4471
      </li>
      <li class="contact-item">
        <svg class="contact-icon" viewBox="0 0 12 12" aria-hidden="true"><path d="M3 0.5h6a1 1 0 0 1 1 1v9a1 1 0 0 1-1 1H3a1 1 0 0 1-1-1v-9a1 1 0 0 1 1-1zm0.3 1.3v7.4h5.4V1.8z"/></svg>
        555 380 1926
      </li>
      <li class="contact-item">
        <svg class="contact-icon" viewBox="0 0 12 12" aria-hidden="true"><path d="M0.5 2.5h11v7h-11zM1.3 3.2L6 6.8l4.7-3.6z"/></svg>
        info@tandrel.com
      </li>
      <li class="contact-item">
        <svg class="contact-icon" viewBox="0 0 12 12" aria-hidden="true"><path d="M6 0.5a5.5 5.5 0 1 0 0 11 5.5 5.5 0 0 0 0-11zm0 1c0.8 0.8 1.3 2.3 1.4 3.9H4.6C4.7 3.8 5.2 2.3 6 1.5zM1.6 5.4a4.5 4.5 0 0 1 2.2-3.3 7 7 0 0 0-0.8 3.3zm7.4 0a7 7 0 0 0-0.8-3.3 4.5 4.5 0 0 1 2.2 3.3zM1.6 6.6H3a7 7 0 0 0 0.8 3.3 4.5 4.5 0 0 1-2.2-3.3zm3 0h2.8C7.3 8.2 6.8 9.7 6 10.5 5.2 9.7 4.7 8.2 4.6 6.6zm4.4 0h1.4a4.5 4.5 0 0 1-2.2 3.3A7 7 0 0 0 9 6.6z"/></svg>
        www.tandrel.com
      </li>
    </ul>
  </section>

  <section class="card card-back">
    <p class="brand-name">Tandrel</p>
  </section>
</body>
</html>
```